Die Morgenfalter - ein Wissenschaftsthriller sucht ein tolles Buchcover
Die Zusammenarbeit war einfach und das Ergebnis war verblüffend genial. Gute Ideen, schnelle Umsetzung und sie versteht es Vorschläge in das Design einfliessen zu lassen! Jederzeit wieder. Sorry für die späte Bewertung.
Zielgruppe
Das Buch (Print und E-Book+Vorschaugrafik) 'Die Morgenfalter' sucht dringend ein neues Cover. Zielgruppe sind sowohl Leser/innen die nach einem spannenden 'High Tech' Thriller in den Buchhandlungen suchen, als auch Leser die einen E-Book Reader benutzen und für relativ wenig Geld auch mal ein Experiment einkaufen (Debütthriller)- Hier muß das Cover sehr schnell 'Aufmerksamkeit' erregen beim blättern im Web und in den Katalogen!
Wichtig ist, es handelt sich nicht um einen reinen Science Fiction Thriller, es ist ein realitätsnahes Buch und soll eine breite Leserschaft ansprechen.
Die Handlung könnte im hier und jetzt spielen, es geht um Quantencomputer, Hacker, Industriespionage, Computerchips und Wirtschaftskriminalität.
Das Buch hat 560 Seiten!
Mehr über das Buch unter www.morgenfalter-roman.com
Hier der Klappentext auf die schnelle:
Das Buch
Fesselnd, abwechslungsreich und informativ. Das Buch skizziert eine beängstigende Verschwörung im Rahmen des weltweiten Cyber- War. Ein Szenario das morgen durchaus Realität werden könnte. Detailliert und brutal beschreibt der Autor wie die Supermächte versuchen die Welt 2.0 zu kontrollieren und zu beherrschen.
+++++++ Die Story +++++++++++++++++++++ Die Story +++++++++++
Felix Obermann arbeitet als Spezialist für Halbleitertechnologie für das Unternehmen Polaris Markt Analytik. Während er für die auf internationales Patentrecht spezialisierte Kanzlei von Ewald Halberg eine Marktanalyse für Netzwerkchips erstellt, erfährt er von einem Informanten, dass der berühmte Wissenschaftler Benedikt Sauer tot in einem Kanal in Bangkok gefunden wurde. Angeblich hat er eine wissenschaftliche Entdeckung mit in sein nasses Grab genommen.
Als Felix Obermann ein Angebot von der Kanzlei Halberg für eine Zusammenarbeit bekommt, ändert sich sein bis dahin eher langweiliges Leben schlagartig. Als Partnerin bekommt er die geheimnisvolle Ilka ter Huis an seine Seite. Der erste ..
Aufgabenstellung
Anbei ein paar alte Cover, Bilder die Sie benutzen können, ein Mastercover wegen Größe von Folio Dock und Texte. Als Ergebnis möchte ich folgendes bekommen:
- Ein Buchcover komplett- fertig und geeignet für den Druck über den Folio Dock Service. Als Art ist matt-glossy meine bevorzugte Einstellung. Die Datei muß .pdf (Druckformat – bitte Farbeinstellung beachten!) sein
- Meine gewählte Buchgröße ist (5,0x8,0 d.h.12,7x20,32), anbei eine Datei die die gesamte Größe darstellt. Es sind insgesamt 280 einzelne Seiten- bei der Berechnung vom Spin beachten! (560 Seiten zum lesen)
- Ein E-Book Cover (.jpg) optimiert für E-Reader (d.h. es sollte nicht so eine riesige Datei sein und insgesamt ein wenig skalierbar hinsichtlich Größe)
- eine Vorschaugrafik von dem Cover (vielleicht 300*500 Pixel o.ä.)
Das Cover sollte sowohl „ Leben“ zeigen (vielleicht ein paar schattierte Menschen i m Hintergrund?), als auch den wissenschaftlichen Hintergrund ( Computerchips etc.)
Aus meiner kleinen Umfrage habe ich folgendes mitgenommen:
Das alte Cover ( nur schwarz mit einer symbolhaften Leiterplatte in rot) erzeugt zu wenig Aufmerksamkeit, zu Langweilig, keine Aussagekraft, zu technisch!
Das zweite Cover mit dem blauen Würfel vorne und der Buchrückseite mit dem Chip ist viel besser, aber immer noch zu „tot“, es fehlt Leben?
Das Pop Art Cover in knallbunt ist wohl der totale Missgriff….;(
Man kann es nicht jedem recht machen, aber Aufmerksamkeit, Technologiebezug und ein wenig Leben auf dem Bild, eine als Druckvorlage geeignete Datei, ein handwerklich gekonntes E-Book Cover Design und eine Vorschaugrafik die auch als solche zu erkennen ist, sollte möglich sein.
Ein wichtiger Hinweis noch: Das Projekt ist dann beendet, wenn die Cover Datei funktioniert bei Folio Dock und das gedruckte Buchcoverokay ist, d.h. wenn es soweit ist, ordere ich ein Buch und die Qualität muss stimmen (Auflösung ..

```html
<!DOCTYPE html>
<html lang="de">
<head>
<meta charset="utf-8">
<title>Die Morgenfalter – Buchumschlag</title>
<link rel="stylesheet" href="https://fonts.googleapis.com/css2?family=Oswald:wght@500;600;700&family=Arimo:wght@400;700&display=swap">
<style>
  :root{
    --ink:#04070d;
    --panel:#070b14;
    --cyan:#27c4f2;
    --cyan-deep:#0a6fb3;
    --glow:#1b5f9e;
    --white:#ffffff;
    --text:#e6edf5;
    --grey:#9aa4ad;
    --rule:#3c4756;
  }
  *{margin:0;padding:0;box-sizing:border-box}
  html,body{width:1200px;height:860px;overflow:hidden;background:var(--ink)}
  .wrap{position:relative;width:1200px;height:860px;background:var(--ink);overflow:hidden}

  /* background art areas */
  .art-back{position:absolute;left:0;top:0;width:512px;height:860px;
    background:radial-gradient(ellipse at 60% 45%, #0d1a2c 0%, var(--panel) 60%, var(--ink) 100%)}
  .art-spine{position:absolute;left:512px;top:0;width:176px;height:860px;
    background:linear-gradient(180deg,#081220 0%, #060a12 100%)}
  .art-front{position:absolute;left:688px;top:0;width:512px;height:860px;
    background:
      radial-gradient(circle at 46% 40%, rgba(39,196,242,.55) 0%, rgba(10,111,179,.45) 18%, rgba(27,95,158,.18) 38%, rgba(4,7,13,0) 62%),
      linear-gradient(180deg,#0b2238 0%, #07101c 22%, #05080f 60%, #0a1626 100%)}
  .art-rain{position:absolute;left:688px;top:0;width:512px;height:170px;
    background:linear-gradient(180deg, rgba(39,196,242,.28) 0%, rgba(39,196,242,.08) 70%, rgba(39,196,242,0) 100%)}

  /* back cover */
  .back{position:absolute;left:36px;top:56px;width:470px;color:var(--text);font-family:"Arimo",Arial,sans-serif}
  .back-headline{font-family:"Oswald",Arial,sans-serif;font-weight:600;font-size:34px;line-height:46px;
    color:var(--white);text-transform:uppercase;letter-spacing:.3px}
  .blurb{margin-top:30px;font-size:13.5px;line-height:17.5px;width:460px}
  .section-title{font-family:"Oswald",Arial,sans-serif;font-weight:600;font-size:28px;line-height:36px;
    color:var(--white);text-transform:uppercase;border-bottom:2px solid var(--rule);padding-bottom:4px;width:460px}
  .reality{margin-top:34px}
  .opinions{margin-top:34px}
  .section-text{margin-top:10px;font-size:13.5px;line-height:17.5px;width:460px}
  .quote + .quote{margin-top:20px}

  /* spine */
  .spine-title,.spine-author{position:absolute;font-family:"Oswald",Arial,sans-serif;font-weight:700;
    text-transform:uppercase;white-space:nowrap;transform-origin:left top;transform:rotate(90deg)}
  .spine-title{left:644px;top:44px;font-size:62px;line-height:68px;color:var(--cyan);letter-spacing:1px}
  .spine-author{left:618px;top:600px;font-size:28px;line-height:34px;color:var(--white)}

  /* front cover */
  .front-author{position:absolute;right:22px;top:26px;font-family:"Oswald",Arial,sans-serif;font-weight:700;
    font-size:34px;line-height:40px;color:var(--white);text-transform:uppercase}
  .front-title{position:absolute;left:744px;top:452px;width:440px;font-family:"Oswald",Arial,sans-serif;
    font-weight:700;text-transform:uppercase;transform:skewX(-8deg) rotate(4deg);transform-origin:left top}
  .front-title .line-1{display:block;font-size:104px;line-height:104px;color:var(--white)}
  .front-title .accent{color:var(--cyan)}
  .front-title .line-2{display:block;font-size:96px;line-height:100px;color:var(--white);padding-left:18px}
  .front-subtitle{display:block;margin-top:6px;padding-left:22px;font-family:"Oswald",Arial,sans-serif;font-weight:500;
    font-size:28px;line-height:34px;color:var(--grey);letter-spacing:1px}
</style>
</head>
<body>
<div class="wrap">
  <div class="art-back" role="img" aria-label="Dunkler Hintergrund mit feinen blauen Leiterbahnen"></div>
  <div class="art-spine" role="img" aria-label="Dunkler Buchrücken mit Leiterbahnen"></div>
  <div class="art-front" role="img" aria-label="Leuchtend blauer Chip-Würfel über einer Leiterplatte"></div>
  <div class="art-rain" role="img" aria-label="Herabfallende blaue Binärziffern"></div>

  <section class="back">
    <h2 class="back-headline">Mord und Intrigen in der Welt der Chip-Technologien</h2>
    <p class="blurb">Eben noch hat Felix Obermann an seinem Schreibtisch in Hamburg eine Marktanalyse für Netzwerkchips erstellt, jetzt findet sich der Spezialist für Halbleitertechnologie plötzlich in einem undurchsichtigen Strudel aus Mord, Korruption und Intrigen wieder. Nach dem mysteriösen Tod eines renommierten amerikanischen Quanteninformatikers in Thailand sollen er und seine Partnerin Ilka ter Huis im Auftrag eines internationalen Konsortiums herausfinden, was es mit einer neuen Generation von Chips auf sich hat – der ermordete Wissenschaftler arbeitete angeblich an deren Herstellung. Noch ahnt Obermann nicht, auf was er sich da eingelassen hat.</p>

    <h3 class="section-title reality">Die Realität!</h3>
    <p class="section-text">Das Buch skizziert eine beängstigende Verschwörung im Rahmen des weltweiten Cyber- War. Ein Szenario das Realität werden könnte. Detailliert und brutal beschreibt der Autor wie die Supermächte versuchen die Welt 2.0 zu kontrollieren und zu beherrschen.</p>

    <h3 class="section-title opinions">Meinungen</h3>
    <div class="section-text">
      <p class="quote">Spannender, zeitgemäßer Wissenschafts-Thriller<br>Jonas Wehrmann hat mit „Die Morgenfalter“ einen realitätsnahen- und spannenden Wissenschaftsthriller geschrieben, der im Genre „Thriller“ einen sicheren Platz einnehmen darf. Er setzt mit seinem Buch eine erschreckende Szenerie der Wissenschaftsspionage ins Bild. (Bücherhafen)</p>
      <p class="quote">Im Kampf um die Macht zählt ein Menschenleben nichts- brisantes Thema gut aufgearbeitet (Lesekreisel)</p>
      <p class="quote">Der Debütroman enthält alle klassischen Elemente eines Thrillers. Es dreht sich gleichermaßen um Forschung, Quanteninformatik und Halbleitertechnik wie um Verschwörung, Korruption und Mord ! Technikblatt 1/15</p>
    </div>
  </section>

  <div class="spine-title">Die Morgenfalter</div>
  <div class="spine-author">Jonas Wehrmann</div>

  <div class="front-author">Jonas Wehrmann</div>
  <h1 class="front-title">
    <span class="line-1">Die <span class="accent">Morgen</span></span>
    <span class="line-2">Falter</span>
    <span class="front-subtitle">Ein Wissenschaftsthriller</span>
  </h1>
</div>
</body>
</html>
```